engineering and fabrication company- KelbroTek

We require a full functional and coded website design for an engineering and fabrication company in Western Australia.
I have attached capability statement with a content of this website.
I would like to have Fabrication services divided into two sections

1. Steel Fabrication
2. Plastic Fabrication

Industry/Entity Type

mining , waste water , oil and gas , engineering and design

Coding

Coded - Design and coding required

Number of Pages Required

5+ page

Colors
0054AA
0677BA
7BADD7
CADEEF
E8F1F8
0094D4
00A9DD
6FCCEA
C7EBF8
E9F6FB

Requirements
Must have
• Must look very professional

```html
<!DOCTYPE html>
<html lang="en">
<head>
<meta charset="utf-8">
<title>KelbroTek — Engineering &amp; Fabrication</title>
<link href="https://fonts.googleapis.com/css2?family=Poppins:ital,wght@0,400;0,500;0,600;0,700;0,800;1,400&display=swap" rel="stylesheet">
<style>
:root{
  --blue-deep:#0054AA;
  --blue:#0677BA;
  --sky:#0094D4;
  --sky-2:#00A9DD;
  --ink:#1b1b1b;
  --text:#555;
  --bg:#f4f4f4;
  --white:#fff;
  --navy:#0b2246;
}
*{box-sizing:border-box;margin:0;padding:0}
html,body{width:1200px;height:4161px;overflow:hidden}
body{font-family:'Poppins',sans-serif;background:var(--bg);color:var(--ink);position:relative}
.abs{position:absolute}
a{color:inherit;text-decoration:none}

/* header */
.topbar{left:0;top:0;width:1200px;height:106px;background:var(--white)}
.brand{left:140px;top:22px;display:flex;align-items:center;gap:8px;font-weight:700;font-size:22px;color:var(--blue-deep)}
.brand i{width:14px;height:14px;background:var(--sky);display:block}
.contact-item{top:16px;font-size:15px;font-weight:500;line-height:1.25;white-space:nowrap}
.contact-item small{display:flex;align-items:center;gap:4px;color:var(--sky);font-size:13px;font-weight:400}
.contact-item svg{width:13px;height:13px}
.divider{top:18px;width:1px;height:42px;background:#ddd}

.nav{left:140px;top:80px;width:920px;height:68px;background:#0a0a0a;border-radius:3px;display:flex;align-items:center;padding:0 44px;z-index:3}
.nav ul{list-style:none;display:flex;gap:40px;font-size:13px;color:#fff;font-weight:500}
.nav li.active{color:var(--sky);position:relative}
.nav li.active:after{content:"";position:absolute;left:0;right:0;bottom:-24px;height:2px;background:var(--sky)}
.btn{display:inline-block;background:var(--sky);color:#fff;font-size:12px;font-weight:500;border-radius:3px;text-align:center}
.nav .btn{margin-left:auto;background:var(--blue-deep);padding:10px 20px}
.nav .search{margin-left:36px;width:22px;height:22px}

/* hero */
.hero{left:0;top:106px;width:1200px;height:600px;background:radial-gradient(ellipse at 30% 75%,#8a5a1a 0%,#3a2c1e 30%,#1d2228 65%,#12161b 100%)}
.hero-title{left:0;width:1200px;text-align:center;font-weight:800;line-height:1.3}
.hero-title .l1{font-size:40px;color:#fff;display:block}
.hero-title .l2{font-size:50px;color:var(--sky);display:block;letter-spacing:1px}
.hero .btn{position:absolute}

/* feature cards */
.features{left:140px;top:613px;width:920px;height:219px;display:flex;z-index:2}
.feature{flex:1;background:var(--white);text-align:center;padding:42px 40px 0;border-left:1px solid #eee}
.feature.photo{background:linear-gradient(160deg,#243244,#101a26 70%,#3a2a18);border:none}
.feature h3{font-size:14px;font-weight:600;color:var(--blue-deep);margin-bottom:16px}
.feature.photo h3{color:var(--sky)}
.feature p{font-size:11px;line-height:1.55;color:#666}
.feature.photo p{color:#fff}
.feature a{display:block;margin-top:28px;font-size:11px;color:var(--sky)}

/* about */
.about-img{left:140px;top:940px;width:380px;height:394px;border-radius:3px;background:radial-gradient(circle at 55% 55%,#c07a2c 0%,#4b3322 35%,#1d2a3a 75%)}
.about{left:565px;top:952px;width:490px}
h2.title{font-size:23px;font-weight:500;line-height:1.6;color:#222;text-transform:uppercase}
.lead{font-size:14.5px;line-height:1.82;color:var(--text);margin-top:16px}
.checks{list-style:none;margin-top:18px}
.checks li{display:flex;align-items:center;gap:16px;font-size:14.5px;font-weight:500;color:#333;height:33px}
.checks svg{width:16px;height:16px}

/* services */
.services{left:0;top:1428px;width:1200px;height:849px;background:radial-gradient(ellipse at 15% 85%,#2c5a8e 0%,#163869 30%,#0c2550 60%,#081c3f 100%);color:#fff}
.services .head{position:absolute;left:0;width:1200px;text-align:center}
.services h2{font-size:23px;font-weight:600}
.services .sub{top:130px;font-size:14.5px;line-height:1.85;width:600px;left:300px}
.svc{position:absolute;width:300px;display:flex;gap:18px}
.svc .ico{flex:0 0 58px;height:58px;border-radius:50%;background:var(--sky);display:flex;align-items:center;justify-content:center}
.svc .ico svg{width:28px;height:28px}
.svc h4{font-size:15px;font-weight:600;line-height:1.5;margin-top:4px}
.svc p{font-size:11px;line-height:1.55;margin-top:4px;width:180px}

/* stats section */
.sec-head{left:0;width:1200px;text-align:center}
.sec-head h2{font-size:23px;font-weight:500;color:#222}
.sec-head p{font-size:14.5px;line-height:1.85;color:var(--text);width:600px;margin:24px auto 0}
.perf{left:140px;top:2572px;width:420px}
.perf .btn{margin-top:48px;padding:11px 37px}
.chart{left:620px;top:2560px;width:440px;height:320px}

.stats-band{left:0;top:3043px;width:1200px;height:118px;background:var(--white)}
.stat{top:2983px;width:210px;height:115px;background:var(--white);box-shadow:0 4px 16px rgba(0,0,0,.07);text-align:center;padding-top:28px}
.stat h5{font-size:13px;font-weight:500;color:#333}
.stat .val{display:flex;justify-content:center;align-items:center;gap:12px;margin-top:10px;font-size:25px;font-weight:500;color:var(--blue-deep)}
.stat svg{width:40px;height:40px}

/* testimonials */
.testi-wrap{left:0;top:3161px;width:1200px;height:735px;background:var(--white)}
.testi{left:140px;top:3225px;width:430px}
.testi h2{font-size:25px;font-weight:500;color:#222}
.rating{display:flex;align-items:center;gap:20px;margin-top:34px;font-size:13px;font-weight:500}
.stars{display:flex;gap:4px}
.stars svg{width:16px;height:16px}
.quote-mark{margin-top:16px;width:120px;height:76px}
.testi .lead{margin-top:8px}
.person{display:flex;align-items:center;gap:24px;margin-top:44px}
.avatar{width:52px;height:52px;border-radius:50%;background:linear-gradient(135deg,#6b5a4c,#2e2a28)}
.person b{display:block;font-size:13px;font-weight:500;color:var(--blue-deep)}
.person i{font-size:13px;color:#444}
.dots{display:flex;gap:8px;margin-top:32px}
.dots span{width:8px;height:8px;border-radius:50%;background:#ccc}
.dots span.on{background:var(--sky)}
.testi-img{left:640px;top:3200px;width:420px;height:527px;background:linear-gradient(120deg,#2d3f5a 0%,#5d6e86 35%,#d8a12a 60%,#f2c515 75%,#c9ccd2 100%)}

/* footer */
.contact-bar{left:140px;top:3850px;width:920px;height:115px;background:#050505;color:#fff;z-index:2}
.contact-bar .contact-item{top:34px}
.contact-bar .divider{top:38px;background:#444}
.footer{left:0;top:3896px;width:1200px;height:265px;background:var(--bg)}
.f-text{left:140px;top:4050px;width:270px;font-size:11px;line-height:1.8;color:#666}
.social{left:140px;top:4117px;display:flex;gap:16px}
.social span{width:10px;height:10px;background:var(--blue-deep);display:block}
.social span:nth-child(2){border-radius:50%}
.links{left:582px;top:4000px;width:480px}
.links h6{font-size:13px;font-weight:600;color:var(--blue-deep)}
.links ul{list-style:none;display:grid;grid-template-columns:225px 225px;row-gap:14px;margin-top:20px}
.links li{display:flex;align-items:center;gap:14px;font-size:11.5px;font-weight:500;color:#333}
.links svg{width:15px;height:15px}
</style>
</head>
<body>

<header class="abs topbar">
  <div class="abs brand"><i></i>KelbroTek</div>
  <div class="abs contact-item" style="left:484px"><small><svg viewBox="0 0 24 24" fill="none" stroke="#0094D4" stroke-width="2"><path d="M5 3h4l2 5-3 2a11 11 0 0 0 6 6l2-3 5 2v4a2 2 0 0 1-2 2A17 17 0 0 1 3 5a2 2 0 0 1 2-2z"/></svg>Contact No</small>018 - 456 - 7290</div>
  <div class="abs divider" style="left:636px"></div>
  <div class="abs contact-item" style="left:662px"><small><svg viewBox="0 0 24 24" fill="none" stroke="#0094D4" stroke-width="2"><rect x="3" y="5" width="18" height="14" rx="2"/><path d="M3 7l9 6 9-6"/></svg>Email</small>hello@kelbrotek.com</div>
  <div class="abs divider" style="left:872px"></div>
  <div class="abs contact-item" style="left:902px"><small><svg viewBox="0 0 24 24" fill="none" stroke="#0094D4" stroke-width="2"><path d="M12 22s7-7 7-12a7 7 0 0 0-14 0c0 5 7 12 7 12z"/><circle cx="12" cy="10" r="2.5"/></svg>Address</small>48 Forge Street</div>
</header>

<nav class="abs nav">
  <ul><li class="active">HOME</li><li>ABOUT</li><li>SERVICES</li><li>PROJECTS</li><li>NEWS</li><li>CONTACT</li></ul>
  <a class="btn">Request a Quote</a>
  <svg class="search" viewBox="0 0 24 24" fill="none" stroke="#fff" stroke-width="2"><circle cx="10" cy="10" r="7"/><path d="M15 15l6 6"/></svg>
</nav>

<section class="abs hero" role="img" aria-label="Welder in safety gear grinding steel with sparks flying">
  <h1 class="abs hero-title" style="top:264px"><span class="l1">WE HELP INDUSTRIES</span><span class="l2">INNOVATE AND GROW</span></h1>
  <a class="btn" style="left:531px;top:406px;width:138px;height:34px;line-height:34px">Learn More</a>
</section>

<div class="abs features">
  <div class="feature photo" role="img" aria-label="Sparks from metal grinding">
    <h3>THE GOLDEN RULE</h3>
    <p>Many say it, but we live by it. From clients to staff, everyone at KelbroTek leads by treating others how they</p>
    <a>Learn More</a>
  </div>
  <div class="feature">
    <h3>QUALITY AND PRECISION</h3>
    <p>The projects that KelbroTek contributes to are largely dependent on the quality and precision of the fabrication</p>
    <a>Learn More</a>
  </div>
  <div class="feature">
    <h3>UNBEATABLE SUPPORT</h3>
    <p>We take customer support seriously, making it our mission to always be upfront with our</p>
    <a>Learn More</a>
  </div>
</div>

<div class="abs about-img" role="img" aria-label="Welder working inside a large steel pipe"></div>
<section class="abs about">
  <h2 class="title">Where innovation<br>meets precision</h2>
  <p class="lead">The work we do at KelbroTek is cutting edge, but every project comes down to how our team handles your needs. That’s why your dedicated project team is with you every step of the way, focusing on your unique design ideas, budget, and schedule.</p>
  <ul class="checks">
    <li><svg viewBox="0 0 24 24" fill="none" stroke="#0094D4" stroke-width="2"><circle cx="12" cy="12" r="10"/><path d="M7 12l3 3 7-7"/></svg>Computer Aided Design</li>
    <li><svg viewBox="0 0 24 24" fill="none" stroke="#0094D4" stroke-width="2"><circle cx="12" cy="12" r="10"/><path d="M7 12l3 3 7-7"/></svg>CNC Capabilities</li>
    <li><svg viewBox="0 0 24 24" fill="none" stroke="#0094D4" stroke-width="2"><circle cx="12" cy="12" r="10"/><path d="M7 12l3 3 7-7"/></svg>Chemical Bunds</li>
    <li><svg viewBox="0 0 24 24" fill="none" stroke="#0094D4" stroke-width="2"><circle cx="12" cy="12" r="10"/><path d="M7 12l3 3 7-7"/></svg>Lining/ Flow Promotion</li>
  </ul>
</section>

<section class="abs services" role="img" aria-label="Dark blue backdrop of sparks from steel cutting">
  <h2 class="head" style="top:82px">WHERE INNOVATION MEETS PRECISION</h2>
  <p class="head sub">The work we do at KelbroTek is cutting edge, but every project comes down to how our team handles your</p>

  <div class="svc" style="left:140px;top:258px"><div class="ico"><svg viewBox="0 0 24 24" fill="none" stroke="#fff" stroke-width="1.6"><circle cx="12" cy="12" r="8"/><path d="M8 12l3 3 5-6"/></svg></div><div><h4>QUALITY AND PRECISION</h4><p>The projects that KelbroTek contributes to are largely dependent on the quality and precision of the fabrication</p></div></div>
  <div class="svc" style="left:447px;top:258px"><div class="ico"><svg viewBox="0 0 24 24" fill="none" stroke="#fff" stroke-width="1.6"><path d="M3 20h18M5 20V10l4 3V10l4 3V6h4v14"/></svg></div><div><h4>Industrial Storage and Process Tanks</h4><p>The projects that KelbroTek contributes to are largely dependent on the quality and precision of the fabrication</p></div></div>
  <div class="svc" style="left:754px;top:258px"><div class="ico"><svg viewBox="0 0 24 24" fill="none" stroke="#fff" stroke-width="1.6"><path d="M7 20V4h6a5 5 0 0 1 0 10H9l6 6"/></svg></div><div><h4>CNC Capabilities</h4><p>The projects that KelbroTek contributes to are largely dependent on the quality and precision of the fabrication</p></div></div>

  <div class="svc" style="left:140px;top:440px"><div class="ico"><svg viewBox="0 0 24 24" fill="none" stroke="#fff" stroke-width="1.6"><path d="M8 3v6h4v4h6v6"/><circle cx="8" cy="3" r="1"/></svg></div><div><h4>Chemical Bunds</h4><p>The projects that KelbroTek contributes to are largely dependent on the quality and precision of the fabrication</p></div></div>
  <div class="svc" style="left:447px;top:440px"><div class="ico"><svg viewBox="0 0 24 24" fill="none" stroke="#fff" stroke-width="1.6"><path d="M4 6h6v6H4zM14 12h6v6h-6zM10 9h4v6"/></svg></div><div><h4>Lining/ Flow Promotion</h4><p>The projects that KelbroTek contributes to are largely dependent on the quality and precision of the fabrication</p></div></div>
  <div class="svc" style="left:754px;top:440px"><div class="ico"><svg viewBox="0 0 24 24" fill="none" stroke="#fff" stroke-width="1.6"><path d="M4 10h16M8 10V5h8v5M6 14h12v6H6z"/></svg></div><div><h4>Onsite Services</h4><p>The projects that KelbroTek contributes to are largely dependent on the quality and precision of the fabrication</p></div></div>

  <div class="svc" style="left:140px;top:628px"><div class="ico"><svg viewBox="0 0 24 24" fill="none" stroke="#fff" stroke-width="1.6"><path d="M8 3h8M9 3v18M15 3v18M7 21h10M9 8h6M9 13h6"/></svg></div><div><h4>Steel Pipe Fabrication</h4><p>The projects that KelbroTek contributes to are largely dependent on the quality and precision of the fabrication</p></div></div>
  <div class="svc" style="left:447px;top:628px"><div class="ico"><svg viewBox="0 0 24 24" fill="none" stroke="#fff" stroke-width="1.6"><circle cx="7" cy="15" r="3"/><circle cx="13" cy="15" r="3"/><circle cx="10" cy="10" r="3"/><path d="M4 19h17"/></svg></div><div><h4>Plastic PIPE SPOOLS</h4><p>The projects that KelbroTek contributes to are largely dependent on the quality and precision of the fabrication</p></div></div>
  <div class="svc" style="left:754px;top:628px"><div class="ico"><svg viewBox="0 0 24 24" fill="none" stroke="#fff" stroke-width="1.6"><path d="M5 20h14M7 20V9h10v11M10 9V5h4v4M10 14h4"/></svg></div><div><h4>Pump Frames &amp; Covers</h4><p>The projects that KelbroTek contributes to are largely dependent on the quality and precision of the fabrication</p></div></div>
</section>

<div class="abs sec-head" style="top:2370px">
  <h2>WHERE INNOVATION MEETS PRECISION</h2>
  <p>The work we do at KelbroTek is cutting edge, but every project comes down to how our team handles your</p>
</div>

<section class="abs perf">
  <h2 class="title">Where innovation<br>meets precision</h2>
  <p class="lead">The work we do at KelbroTek is cutting edge, but every project comes down to how our team handles your needs. That’s why your dedicated project team is with you every step of the way, focusing on your unique design ideas, budget, and schedule.<br>Our turnkey fabrication services range from the design</p>
  <a class="btn">Learn More</a>
</section>

<svg class="abs chart" viewBox="0 0 440 320" font-family="Poppins, sans-serif" font-size="10" fill="#888">
  <g stroke="#eee">
    <line x1="62" y1="9" x2="430" y2="9"/><line x1="62" y1="28" x2="430" y2="28"/><line x1="62" y1="46" x2="430" y2="46"/><line x1="62" y1="65" x2="430" y2="65"/><line x1="62" y1="84" x2="430" y2="84"/><line x1="62" y1="102" x2="430" y2="102"/><line x1="62" y1="121" x2="430" y2="121"/><line x1="62" y1="140" x2="430" y2="140"/><line x1="62" y1="158" x2="430" y2="158"/><line x1="62" y1="177" x2="430" y2="177"/><line x1="62" y1="196" x2="430" y2="196"/><line x1="62" y1="214" x2="430" y2="214"/><line x1="62" y1="233" x2="430" y2="233"/><line x1="62" y1="252" x2="430" y2="252"/><line x1="62" y1="270" x2="430" y2="270"/><line x1="62" y1="289" x2="430" y2="289"/>
  </g>
  <line x1="62" y1="9" x2="62" y2="289" stroke="#bbb"/>
  <g text-anchor="end">
    <text x="36" y="12">4300</text><text x="36" y="31">4200</text><text x="36" y="49">4100</text><text x="36" y="68">4000</text><text x="36" y="87">3900</text><text x="36" y="105">3800</text><text x="36" y="124">3700</text><text x="36" y="143">3600</text><text x="36" y="161">3500</text><text x="36" y="180">3400</text><text x="36" y="199">3300</text><text x="36" y="217">3200</text><text x="36" y="236">3100</text><text x="36" y="255">3000</text><text x="36" y="273">2900</text><text x="36" y="292">2800</text>
  </g>
  <rect x="83" y="13" width="40" height="276" fill="#0094D4"/>
  <rect x="157" y="86" width="40" height="203" fill="#0054AA"/>
  <rect x="230" y="160" width="40" height="129" fill="#0094D4"/>
  <rect x="305" y="252" width="40" height="37" fill="#0054AA"/>
  <rect x="382" y="104" width="40" height="185" fill="#0094D4"/>
  <g text-anchor="middle"><text x="103" y="306">Jan</text><text x="177" y="306">Feb</text><text x="250" y="306">Mar</text><text x="325" y="306">Apr</text><text x="402" y="306">May</text></g>
</svg>

<div class="abs stats-band"></div>
<div class="abs stat" style="left:140px"><h5>Construction Workers</h5><div class="val"><svg viewBox="0 0 40 40" fill="none" stroke="#0054AA" stroke-width="2"><path d="M6 26a14 14 0 0 1 28 0z"/><path d="M3 26h34M20 12v14M12 16v10M28 16v10"/><path d="M10 30a10 6 0 0 0 20 0"/></svg>2300+</div></div>
<div class="abs stat" style="left:376px"><h5>Chemical Projects</h5><div class="val"><svg viewBox="0 0 40 40" fill="none" stroke="#0054AA" stroke-width="2"><path d="M10 4h8v12h10v16h-8V22H10z"/><path d="M8 4h12M18 36h12"/></svg>5400+</div></div>
<div class="abs stat" style="left:612px"><h5>Plastic Projects</h5><div class="val"><svg viewBox="0 0 40 40" fill="none" stroke="#0054AA" stroke-width="2"><circle cx="9" cy="26" r="5"/><circle cx="20" cy="26" r="5"/><circle cx="31" cy="26" r="5"/><circle cx="14.5" cy="17" r="5"/><circle cx="25.5" cy="17" r="5"/><path d="M2 33h36"/></svg>87540+</div></div>
<div class="abs stat" style="left:848px"><h5>Steel Pipe Projects</h5><div class="val"><svg viewBox="0 0 40 40" fill="none" stroke="#0054AA" stroke-width="2"><path d="M12 4h16M14 4v32M26 4v32M10 36h20M14 12h12M14 20h12M14 28h12"/></svg>57800+</div></div>

<div class="abs testi-wrap"></div>
<section class="abs testi">
  <h2>Testimonials</h2>
  <div class="rating">Average customer rating
    <div class="stars">
      <svg viewBox="0 0 24 24" fill="#f5b400"><path d="M12 2l3 7 7 .6-5.3 4.7 1.6 7.2L12 17.8 5.7 21.5l1.6-7.2L2 9.6 9 9z"/></svg>
      <svg viewBox="0 0 24 24" fill="#f5b400"><path d="M12 2l3 7 7 .6-5.3 4.7 1.6 7.2L12 17.8 5.7 21.5l1.6-7.2L2 9.6 9 9z"/></svg>
      <svg viewBox="0 0 24 24" fill="#f5b400"><path d="M12 2l3 7 7 .6-5.3 4.7 1.6 7.2L12 17.8 5.7 21.5l1.6-7.2L2 9.6 9 9z"/></svg>
      <svg viewBox="0 0 24 24" fill="#f5b400"><path d="M12 2l3 7 7 .6-5.3 4.7 1.6 7.2L12 17.8 5.7 21.5l1.6-7.2L2 9.6 9 9z"/></svg>
      <svg viewBox="0 0 24 24" fill="#f5b400"><path d="M12 2l3 7 7 .6-5.3 4.7 1.6 7.2L12 17.8 5.7 21.5l1.6-7.2L2 9.6 9 9z"/></svg>
    </div>
  </div>
  <svg class="quote-mark" viewBox="0 0 120 76" fill="#E8F1F8"><path d="M0 0h52v44L34 76H14l12-30H0zM64 0h52v44L98 76H78l12-30H64z"/></svg>
  <p class="lead">The work we do at KelbroTek is cutting edge, but every project comes down to how our team handles your needs. That’s why your dedicated project team is with you every step of the way, focusing on your unique design ideas, budget, and schedule.<br>Our turnkey fabrication services range from the design</p>
  <div class="person"><div class="avatar" role="img" aria-label="Client portrait"></div><div><b>Marcus Ellery</b><i>SEO Expert.</i></div></div>
  <div class="dots"><span></span><span class="on"></span><span></span><span></span></div>
</section>
<div class="abs testi-img" role="img" aria-label="Worker in hi-vis vest holding a yellow hard hat"></div>

<footer class="abs footer"></footer>
<div class="abs contact-bar">
  <div class="abs contact-item" style="left:166px"><small><svg viewBox="0 0 24 24" fill="none" stroke="#0094D4" stroke-width="2"><path d="M5 3h4l2 5-3 2a11 11 0 0 0 6 6l2-3 5 2v4a2 2 0 0 1-2 2A17 17 0 0 1 3 5a2 2 0 0 1 2-2z"/></svg>Contact No</small>018 - 456 - 7290</div>
  <div class="abs divider" style="left:326px"></div>
  <div class="abs contact-item" style="left:356px"><small><svg viewBox="0 0 24 24" fill="none" stroke="#0094D4" stroke-width="2"><rect x="3" y="5" width="18" height="14" rx="2"/><path d="M3 7l9 6 9-6"/></svg>Email</small>hello@kelbrotek.com</div>
  <div class="abs divider" style="left:566px"></div>
  <div class="abs contact-item" style="left:598px"><small><svg viewBox="0 0 24 24" fill="none" stroke="#0094D4" stroke-width="2"><path d="M12 22s7-7 7-12a7 7 0 0 0-14 0c0 5 7 12 7 12z"/><circle cx="12" cy="10" r="2.5"/></svg>Address</small>48 Forge Street</div>
</div>
<div class="abs brand" style="top:3995px"><i></i>KelbroTek</div>
<p class="abs f-text">The work we do at KelbroTek is cutting edge, but every project comes down to how our team</p>
<div class="abs social"><span></span><span></span><span></span></div>
<div class="abs links">
  <h6>Useful Links</h6>
  <ul>
    <li><svg viewBox="0 0 24 24" fill="none" stroke="#0094D4" stroke-width="2"><circle cx="12" cy="12" r="10"/><path d="M7 12l3 3 7-7"/></svg>Home</li>
    <li><svg viewBox="0 0 24 24" fill="none" stroke="#0094D4" stroke-width="2"><circle cx="12" cy="12" r="10"/><path d="M7 12l3 3 7-7"/></svg>About Us</li>
    <li><svg viewBox="0 0 24 24" fill="none" stroke="#0094D4" stroke-width="2"><circle cx="12" cy="12" r="10"/><path d="M7 12l3 3 7-7"/></svg>Corporate Profile</li>
    <li><svg viewBox="0 0 24 24" fill="none" stroke="#0094D4" stroke-width="2"><circle cx="12" cy="12" r="10"/><path d="M7 12l3 3 7-7"/></svg>Portfolio</li>
    <li><svg viewBox="0 0 24 24" fill="none" stroke="#0094D4" stroke-width="2"><circle cx="12" cy="12" r="10"/><path d="M7 12l3 3 7-7"/></svg>Our Team</li>
    <li><svg viewBox="0 0 24 24" fill="none" stroke="#0094D4" stroke-width="2"><circle cx="12" cy="12" r="10"/><path d="M7 12l3 3 7-7"/></svg>Contact Us</li>
  </ul>
</div>

</body>
</html>
```